Product Introduction Brochure

Brochure to introduce our mid/high end lighting products to potential wholesalers / Disrtibutors / Retailers. To be mainly graphical but will contain some text also. The purpose of the brochure will be to get potential customers to find out more either by calling us or to visit our website. The brochure should be of A3 size folded in half to an A4. Front page should be mainly logo and name, inner 2 pages should showcase some of the products we can supply together with some text (to be supplied, please use filler text in the initial design), then the back page containing our contact details. The products are lights, floor lamps and table lamps. I have attached a number of images, as well as our company logo. I would prefer the design to be on a black background, however this is not critical
Target Market(s)
Retailer, distribution and wholesale buyers
Interior design consultants and specifiers
Industry/Entity Type
Product
Look and feel
Each slider illustrates characteristics of the customer's brand and the style your logo design should communicate.

```html
<!DOCTYPE html>
<html lang="en">
<head>
<meta charset="utf-8">
<title>Lumora – Product Brochure Cover Spread</title>
<link rel="stylesheet" href="https://fonts.googleapis.com/css2?family=Open+Sans:wght@400;600;700&display=swap">
<style>
  :root {
    --stage: #d9d9d9;
    --sheet: #050505;
    --fold: #161616;
    --brand-green: #2f9e4a;
    --contact-white: #f2f2f2;
    --contact-orange: #e8921c;
    --shade-light: #f3f0ea;
    --shade-mid: #d9d4cb;
    --shade-metal: #a9a6a0;
  }
  * { margin: 0; padding: 0; box-sizing: border-box; }
  html, body {
    width: 1200px;
    height: 847px;
    overflow: hidden;
    background: var(--stage);
    font-family: "Open Sans", Arial, sans-serif;
  }
  .spread {
    position: absolute;
    left: 60px;
    top: 42px;
    width: 1080px;
    height: 764px;
    display: flex;
    background: var(--sheet);
    box-shadow: 0 18px 40px rgba(0, 0, 0, 0.35);
  }
  .panel {
    position: relative;
    width: 540px;
    height: 764px;
    overflow: hidden;
  }
  .panel--back { border-right: 1px solid var(--fold); }
  .panel--front {
    background: linear-gradient(100deg, rgba(255,255,255,0.05) 0%, rgba(255,255,255,0) 30%);
  }

  .brand {
    position: absolute;
    display: flex;
    align-items: center;
    color: var(--brand-green);
    font-weight: 700;
    line-height: 1;
    white-space: nowrap;
  }
  .brand__dot {
    border-radius: 50%;
    background: var(--brand-green);
    flex: none;
  }
  .brand--small { top: 62px; right: 60px; gap: 10px; font-size: 28px; }
  .brand--small .brand__dot { width: 40px; height: 40px; }
  .brand--large { top: 108px; left: 50%; transform: translateX(-50%); gap: 16px; font-size: 46px; }
  .brand--large .brand__dot { width: 70px; height: 70px; }

  .product-photo { position: absolute; display: block; }
  .product-photo--floor-lamp { left: 40px; top: 100px; width: 230px; height: 470px; }
  .product-photo--pendant { left: 150px; top: 200px; width: 240px; height: 330px; }

  .contact {
    position: absolute;
    left: 0;
    right: 0;
    bottom: 80px;
    text-align: center;
  }
  .contact__label {
    color: var(--contact-white);
    font-size: 14px;
    letter-spacing: 1.5px;
    font-weight: 400;
  }
  .contact__details {
    margin-top: 6px;
    color: var(--contact-orange);
    font-size: 18px;
    letter-spacing: 5px;
  }
  .contact__amp { color: var(--contact-white); }
</style>
</head>
<body>
  <main class="spread">
    <section class="panel panel--back" aria-label="Back cover">
      <div class="brand brand--small">
        <span class="brand__dot"></span>
        <span class="brand__name">Lumora</span>
      </div>

      <svg class="product-photo product-photo--floor-lamp" viewBox="0 0 230 470" role="img" aria-label="Photo of a white floor lamp with a ribbed lantern shade hanging from a curved metal tripod stand">
        <defs>
          <radialGradient id="floorLampTone" cx="0.42" cy="0.2" r="0.75" fx="0.42" fy="0.16">
            <stop offset="0" stop-color="var(--shade-light)"/>
            <stop offset="0.22" stop-color="var(--shade-mid)"/>
            <stop offset="0.5" stop-color="var(--shade-metal)" stop-opacity="0.45"/>
            <stop offset="1" stop-color="var(--sheet)" stop-opacity="0"/>
          </radialGradient>
        </defs>
        <rect width="230" height="470" rx="115" fill="url(#floorLampTone)"/>
      </svg>

      <div class="contact">
        <p class="contact__label">CONTACT US NOW:</p>
        <p class="contact__details">098765432 <span class="contact__amp">&amp;</span> lumora.com</p>
      </div>
    </section>

    <section class="panel panel--front" aria-label="Front cover">
      <div class="brand brand--large">
        <span class="brand__dot"></span>
        <span class="brand__name">Lumora</span>
      </div>

      <svg class="product-photo product-photo--pendant" viewBox="0 0 240 330" role="img" aria-label="Photo of a white ribbed globe pendant lamp hanging from a thin cord">
        <defs>
          <radialGradient id="pendantTone" cx="0.5" cy="0.7" r="0.55" fx="0.45" fy="0.64">
            <stop offset="0" stop-color="var(--shade-light)"/>
            <stop offset="0.32" stop-color="var(--shade-mid)"/>
            <stop offset="0.6" stop-color="var(--shade-metal)" stop-opacity="0.35"/>
            <stop offset="1" stop-color="var(--sheet)" stop-opacity="0"/>
          </radialGradient>
        </defs>
        <rect width="240" height="330" rx="120" fill="url(#pendantTone)"/>
      </svg>
    </section>
  </main>
</body>
</html>
```